Business card for a new cabinet shop company named Marlowe Cabinets for high end cabinets

Design a business card, thinking dark rich green with colours to speak of high end luxury ie; cream, gold, black possibly

Peter Lindqvar
Director Craftsman
Email: info@marlowecabinets.com.au
Instagram : @marlowe.cabinets

```html
<!DOCTYPE html>
<html lang="en">
<head>
<meta charset="utf-8">
<title>Marlowe Cabinets – Business Card</title>
<link rel="stylesheet" href="https://fonts.googleapis.com/css2?family=Poppins:wght@300;400;500;600&display=swap">
<style>
  :root {
    --page-bg: #d9d4cc;
    --card-frost-top: #f3f1ee;
    --card-frost-bottom: #e2dfdb;
    --card-edge: #b8b2aa;
    --ink: #151515;
    --band: #111111;
    --band-soft: #1c1c1c;
    --gold: #a67c3d;
    --gold-light: #c9a15e;
    --copper: #b8683a;
    --cream: #efe6d8;
    --contact-text: #e4d9c8;
  }
  * { margin: 0; padding: 0; box-sizing: border-box; }
  html, body {
    width: 1200px;
    height: 970px;
    overflow: hidden;
    background: var(--page-bg);
    font-family: "Poppins", sans-serif;
  }
  .business-card {
    position: absolute;
    left: 70px;
    top: 183px;
    width: 1060px;
    height: 604px;
    background: linear-gradient(180deg, var(--card-frost-top), var(--card-frost-bottom));
    border: 1px solid var(--card-edge);
    overflow: hidden;
  }
  .brand {
    position: absolute;
    left: 0;
    right: 0;
    top: 130px;
    display: flex;
    align-items: center;
    justify-content: center;
    gap: 22px;
  }
  .brand-mark {
    width: 34px;
    height: 34px;
    background: var(--ink);
  }
  .brand-name {
    font-weight: 500;
    font-size: 64px;
    letter-spacing: 1px;
    color: var(--ink);
    line-height: 1;
  }
  .contact-band {
    position: absolute;
    left: 0;
    right: 0;
    top: 331px;
    height: 223px;
    background: linear-gradient(180deg, var(--band-soft), var(--band) 60%);
    border-top: 7px solid var(--gold);
    border-bottom: 7px solid var(--gold);
  }
  .person {
    position: absolute;
    right: calc(100% - 452px);
    top: 72px;
    text-align: right;
  }
  .person-name {
    font-weight: 600;
    font-size: 33px;
    color: var(--cream);
    line-height: 1.1;
  }
  .person-role {
    font-weight: 400;
    font-size: 22px;
    color: var(--gold);
    line-height: 1.3;
  }
  .divider {
    position: absolute;
    left: 481px;
    top: 56px;
    width: 2px;
    height: 92px;
    background: var(--copper);
  }
  .contact-list {
    position: absolute;
    left: 508px;
    top: 48px;
    list-style: none;
  }
  .contact-item {
    display: flex;
    align-items: center;
    gap: 14px;
    height: 34px;
    font-weight: 300;
    font-size: 25px;
    color: var(--contact-text);
  }
  .contact-icon {
    width: 20px;
    height: 20px;
    flex: none;
    fill: var(--copper);
  }
  .social-dot {
    width: 18px;
    height: 18px;
    margin: 0 1px;
    border-radius: 50%;
    background: var(--copper);
    flex: none;
  }
</style>
</head>
<body>
  <main class="business-card">
    <div class="brand">
      <span class="brand-mark"></span>
      <span class="brand-name">Marlowe Cabinets</span>
    </div>

    <section class="contact-band">
      <div class="person">
        <p class="person-name">Peter Lindqvar</p>
        <p class="person-role">Craftsman</p>
      </div>
      <span class="divider"></span>
      <ul class="contact-list">
        <li class="contact-item">
          <svg class="contact-icon" viewBox="0 0 24 24" aria-hidden="true">
            <path d="M7 2h3l1.5 5-2.5 1.5c1 2.5 3 4.5 5.5 5.5L16 11.5l5 1.5v3c0 1.5-1.2 3-3 3C10 19 5 14 5 6c0-1.8 1-4 2-4z"/>
          </svg>
          (123) 456-7890
        </li>
        <li class="contact-item">
          <svg class="contact-icon" viewBox="0 0 24 24" aria-hidden="true">
            <path d="M2 5h20v14H2z M3.5 6.5 12 13l8.5-6.5v-.2H3.5z" fill-rule="evenodd"/>
          </svg>
          info@marlowecabinets.com.au
        </li>
        <li class="contact-item">
          <span class="social-dot"></span>
          @marlowe.cabinets
        </li>
      </ul>
    </section>
  </main>
</body>
</html>
```